Ebook Design for Brightmoor Wellworks (Health and Dietary Supplements)

Brightmoor Wellworks is an exciting new company in the area of health and wellness. Health requires a multi-dimensional, interdisciplinary approach that encompasses a complete lifestyle. Our company believes in whole-health that incorporates the entire body to ultimately help you live better and longer. We invest in products that boost metabolic functions, enhance natural performance, and support a healthy lifespan. We need a design for our research eBook on our products that sticks true to our brand identity. Please use the colors royal blue and yellow.

```html
<!DOCTYPE html>
<html lang="en">
<head>
<meta charset="utf-8">
<title>Brightmoor Wellworks — Health and Dietary Supplements eBook Cover</title>
<link rel="stylesheet" href="https://fonts.googleapis.com/css2?family=Oswald:wght@400;700&family=Roboto+Condensed:wght@400;500;700&display=swap">
<style>
  :root {
    --royal-blue: #1a2f9c;
    --deep-blue: #1b2a8a;
    --gold: #f6c549;
    --paper: #ffffff;
  }
  html, body {
    margin: 0;
    padding: 0;
    overflow: hidden;
    background: var(--paper);
  }
  .cover {
    position: relative;
    width: 752px;
    height: 1200px;
    overflow: hidden;
    background: var(--paper);
  }
  .cover__art {
    position: absolute;
    inset: 0;
    width: 752px;
    height: 1200px;
    display: block;
  }
  .brand {
    position: absolute;
    top: 30px;
    left: 0;
    width: 752px;
    display: flex;
    justify-content: center;
    align-items: center;
    gap: 10px;
  }
  .brand__dot {
    width: 22px;
    height: 22px;
    border-radius: 50%;
    background: var(--royal-blue);
  }
  .brand__name {
    font-family: "Roboto Condensed", sans-serif;
    font-weight: 700;
    font-size: 19px;
    letter-spacing: 2px;
    color: var(--royal-blue);
    text-transform: uppercase;
  }
  .title {
    position: absolute;
    left: 136px;
    top: 92px;
    margin: 0;
    color: var(--royal-blue);
  }
  .title__lead {
    display: block;
    font-family: "Roboto Condensed", sans-serif;
    font-weight: 500;
    font-size: 80px;
    line-height: 84px;
  }
  .title__main {
    display: block;
    font-family: "Oswald", sans-serif;
    font-weight: 700;
    font-size: 124px;
    line-height: 116px;
    letter-spacing: 1px;
  }
  .subtitle {
    position: absolute;
    left: 70px;
    top: 292px;
    margin: 0;
    font-family: "Roboto Condensed", sans-serif;
    font-weight: 500;
    font-size: 49px;
    color: var(--royal-blue);
    white-space: nowrap;
  }
</style>
</head>
<body>
<div class="cover">
  <svg class="cover__art" viewBox="0 0 752 1200" xmlns="http://www.w3.org/2000/svg">
    <defs>
      <linearGradient id="sketchTone" x1="0" y1="0" x2="0" y2="1">
        <stop offset="0" stop-color="#f1ede6"/>
        <stop offset="1" stop-color="#ffffff"/>
      </linearGradient>
      <linearGradient id="herbTone" x1="0" y1="0" x2="1" y2="1">
        <stop offset="0" stop-color="#c9bba6"/>
        <stop offset="0.35" stop-color="#8a6a3c"/>
        <stop offset="0.6" stop-color="#a2541f"/>
        <stop offset="1" stop-color="#4f7f34"/>
      </linearGradient>
      <linearGradient id="photoFade" x1="0" y1="0" x2="0" y2="1">
        <stop offset="0" stop-color="#ffffff" stop-opacity="1"/>
        <stop offset="1" stop-color="#ffffff" stop-opacity="0"/>
      </linearGradient>
    </defs>

    <rect class="sketch-backdrop" x="0" y="0" width="740" height="720" fill="url(#sketchTone)" opacity="0.8"
          role="img" aria-label="Faint anatomical line sketch of a human figure in a circle"/>

    <path class="herb-photo" d="M0,400 L740,400 L740,700 C705,900 560,1075 270,1200 L0,1200 Z"
          fill="url(#herbTone)" opacity="0.9"
          role="img" aria-label="Photo of an antique brass balance scale, an amber apothecary bottle, an iron pot and fresh green herbs"/>
    <rect class="herb-photo__fade" x="0" y="400" width="740" height="80" fill="url(#photoFade)"/>

    <path class="wave wave--gold" d="M740,0 L752,0 L752,1200 L270,1200 C560,1075 705,900 740,700 Z" fill="var(--gold)"/>
    <path class="wave wave--blue" d="M752,820 C720,980 620,1110 420,1200 L752,1200 Z" fill="var(--deep-blue)"/>
  </svg>

  <div class="brand">
    <span class="brand__dot"></span>
    <span class="brand__name">Brightmoor Wellworks</span>
  </div>

  <h1 class="title">
    <span class="title__lead">The</span>
    <span class="title__main">TITLE</span>
  </h1>
  <p class="subtitle">Health and Dietary Supplements.</p>
</div>
</body>
</html>
```